Qorvane Management LLC Business Card

The sample logo was attached for the business Card Design for Traffic Control Company named Qorvane Management LLC. Card design needs to have the company logo and colors match the logo color. It will be nice to show some images of Traffic control signs or cones, even roads closer that math the company services

Target Market(s)

Temporary traffic control. Road closer.

Industry/Entity Type

Construction

Contact Information for Business Card

basic information, name, job title, address, email phone, website

Font styles to use
Serif
Sans Serif

Colors
F0912C
F2A743
F7CA91
FBE8D2
FDF5EE
EE7325
F08F49
F5BC92
FAE3D3
FDF4ED

```html
<!DOCTYPE html>
<html lang="en">
<head>
<meta charset="utf-8">
<title>Qorvane Management LLC Business Card</title>
<link href="https://fonts.googleapis.com/css2?family=Montserrat:wght@400;500;700&display=swap" rel="stylesheet">
<style>
  :root {
    --backdrop: #161616;
    --card: #242424;
    --orange: #ee7325;
    --white: #ffffff;
  }
  * { box-sizing: border-box; margin: 0; padding: 0; }
  html, body { width: 1200px; height: 900px; overflow: hidden; }
  body {
    background: var(--backdrop);
    font-family: "Montserrat", sans-serif;
    position: relative;
  }
  .card {
    position: absolute;
    left: 240px;
    width: 720px;
    height: 400px;
    background: var(--card);
    border-bottom: 6px solid var(--orange);
    overflow: hidden;
  }
  .card--front { top: 45px; }
  .card--back { top: 465px; }

  .wordmark { color: var(--orange); font-weight: 700; line-height: 1; }
  .wordmark__name { display: block; letter-spacing: 2px; }
  .wordmark__sub { display: block; margin-top: 10px; }

  .card--front .wordmark {
    position: absolute; left: 0; right: 0; top: 140px; text-align: center;
  }
  .card--front .wordmark__name { font-size: 86px; }
  .card--front .wordmark__sub { font-size: 30px; letter-spacing: 4px; }

  .card--back .wordmark {
    position: absolute; left: 44px; top: 142px; width: 300px; text-align: center;
  }
  .card--back .wordmark__name { font-size: 50px; letter-spacing: 1px; }
  .card--back .wordmark__sub { font-size: 18px; letter-spacing: 2px; margin-top: 8px; }

  .divider {
    position: absolute; left: 366px; top: 100px; width: 2px; height: 200px;
    background: var(--orange);
  }
  .contact {
    position: absolute; left: 390px; top: 104px; width: 300px; color: var(--white);
  }
  .contact__name {
    color: var(--orange); font-weight: 700; font-size: 30px; letter-spacing: 1px; line-height: 1.1;
  }
  .contact__title { font-size: 16px; font-weight: 500; margin: 2px 0 12px; }
  .contact__line {
    font-size: 16px; line-height: 1.45; display: flex; align-items: center; gap: 8px; white-space: nowrap;
  }
  .contact__line svg { width: 13px; height: 13px; flex: none; }
  .contact__address { margin-bottom: 8px; }
</style>
</head>
<body>
  <section class="card card--front">
    <div class="wordmark">
      <span class="wordmark__name">QORVANE</span>
      <span class="wordmark__sub">MANAGEMENT LLC</span>
    </div>
  </section>

  <section class="card card--back">
    <div class="wordmark">
      <span class="wordmark__name">QORVANE</span>
      <span class="wordmark__sub">MANAGEMENT LLC</span>
    </div>
    <div class="divider"></div>
    <div class="contact">
      <div class="contact__name">DORIAN VELL</div>
      <div class="contact__title">CEO/Founder</div>
      <div class="contact__address">
        <div class="contact__line">1870 Halden Street</div>
        <div class="contact__line">Fresno, CA 93721</div>
      </div>
      <div class="contact__line">
        <svg viewBox="0 0 16 16"><path d="M4 1l3 3-2 2c1 2 3 4 5 5l2-2 3 3-2 3C7 15 1 9 1 3z" fill="var(--orange)"/></svg>
        555-204-7719
      </div>
      <div class="contact__line">
        <svg viewBox="0 0 16 16"><rect x="1" y="3" width="14" height="10" fill="none" stroke="var(--orange)" stroke-width="1.6"/><path d="M1 3l7 6 7-6" fill="none" stroke="var(--orange)" stroke-width="1.6"/></svg>
        info@QorvaneManagement.com
      </div>
      <div class="contact__line">
        <svg viewBox="0 0 16 16"><circle cx="8" cy="8" r="6.5" fill="none" stroke="var(--orange)" stroke-width="1.4"/><ellipse cx="8" cy="8" rx="3" ry="6.5" fill="none" stroke="var(--orange)" stroke-width="1.2"/><path d="M1.5 8h13" stroke="var(--orange)" stroke-width="1.2"/></svg>
        www.QorvaneManagement.com
      </div>
    </div>
  </section>
</body>
</html>
```